family chiropractic health care team needs a modern business card design

Healthcare office with Chiropractors, Physiotherapists, Massage therapists and possibly other practitioners in the future. This is a friendly family office with patients of all ages (and lots of kids) that just moved into a new larger modern office.
Look at the website for photos of the office.
Design for the front and back of a business card required.
Text for the front:
Office logo and name of the office:
Bright Path Wellness Centre
Name of current Practitioner:
Dr. Marten Quovel B.Sc., D.C. Chiropractor
(But please include options to swap out name and title for other practitioners )

address:
218 Farrow Gate
Larkmoor WC.
K2J 6P4
Phone: 416-872-0196 (PATH)
Web site and email:
www.brightpathwellnesscentre.example
brightpathchiro@mailbox.example

2 versions of the back of the card:
1. text below
2. appointment schedule card

Text on back of card:
Chiropractic Card text on back of the card:
There is more to chiropractic than the relief of headaches and back pain! Our primary focus is the integrity of your nerve system, which controls and regulates every cell and tissue of your body. The moving bones of the spinal column can impair this vital communication link between your brain and body. We help improve the function and structure of your spine, reducing nerve system compromise. The result?
Even non-spinal related health problems can show improvement
without drugs
without surgery
regardless of age
for over a century
naturally

Appointment Card info For Back:
Please integrate design elements from the front of the card into an appointment card format.
M Tu W Th F Sat (and a line for writing on beside each one)

```html
<!DOCTYPE html>
<html lang="en">
<head>
<meta charset="utf-8">
<title>Bright Path Wellness Centre – Business Cards</title>
<link href="https://fonts.googleapis.com/css2?family=Cinzel:wght@400;700&family=EB+Garamond:wght@400;500&display=swap" rel="stylesheet">
<style>
  :root {
    --page-bg: #1c1c1c;
    --card-bg: #2c2c2c;
    --green: #8dc63f;
    --ink-light: #ececec;
    --ink-muted: #a4a4a4;
    --rule: #5a5a5a;
    --paper: #ffffff;
    --ink-dark: #333333;
  }
  * { box-sizing: border-box; margin: 0; padding: 0; }
  html, body { width: 818px; height: 1200px; overflow: hidden; background: var(--page-bg); }
  body { position: relative; font-family: "EB Garamond", Georgia, serif; }

  .card {
    position: absolute;
    width: 480px; height: 274px;
    border-radius: 14px;
    background: linear-gradient(160deg, #343434 0%, var(--card-bg) 55%, #262626 100%);
    box-shadow: 0 10px 28px rgba(0,0,0,.55);
    overflow: hidden;
  }
  .card--info    { left: 40px;  top: 30px; }
  .card--front-1 { left: 298px; top: 300px; }
  .card--appt    { left: 40px;  top: 630px; }
  .card--front-2 { left: 298px; top: 900px; }

  /* Wordmark */
  .wordmark { position: absolute; text-align: center; font-family: "Cinzel", Georgia, serif; font-weight: 700; color: var(--green); line-height: 1; }
  .wordmark__main { display: block; font-size: 27px; letter-spacing: 1px; }
  .wordmark__sub { display: block; font-size: 11px; letter-spacing: 6px; margin-top: 6px; }

  /* Info back */
  .card--info .wordmark { left: 0; right: 0; top: 30px; }
  .info__copy { position: absolute; left: 38px; right: 38px; top: 92px; text-align: center; color: var(--green); font-size: 10.6px; line-height: 1.32; }
  .info__result { margin-top: 6px; }
  .info__benefits { position: absolute; left: 20px; right: 20px; bottom: 24px; display: flex; justify-content: center; gap: 8px; color: var(--ink-light); font-size: 11px; }
  .info__benefits .sep { color: var(--ink-muted); }

  /* Front */
  .card--front-1 .wordmark, .card--front-2 .wordmark { left: 40px; top: 42px; text-align: left; }
  .practitioner { position: absolute; left: 40px; top: 114px; }
  .practitioner__name { font-family: "Cinzel", Georgia, serif; color: var(--ink-light); font-size: 14.5px; letter-spacing: .3px; }
  .practitioner__title { font-family: "Cinzel", Georgia, serif; color: var(--green); font-size: 12px; letter-spacing: .5px; margin-top: 2px; }
  .front__rule { position: absolute; left: 40px; right: 30px; top: 158px; border-top: 1px solid var(--rule); }
  .contacts { position: absolute; left: 40px; top: 170px; list-style: none; color: var(--ink-light); font-size: 12px; line-height: 1.55; }
  .contacts li { display: flex; align-items: center; gap: 7px; }
  .contacts svg { width: 10px; height: 10px; fill: var(--green); flex: none; }
  .address { position: absolute; right: 30px; top: 170px; text-align: right; color: var(--ink-light); font-size: 12px; line-height: 1.35; font-style: normal; }

  /* Appointment back */
  .appt__waves { position: absolute; inset: 0; }
  .card--appt .wordmark { left: 0; right: 0; top: 24px; }
  .appt__form { position: absolute; left: 30px; right: 30px; top: 150px; color: var(--ink-dark); font-size: 12px; }
  .appt__line { display: flex; align-items: flex-end; gap: 6px; }
  .appt__line .fill { flex: 1; border-bottom: 1px solid #777; height: 12px; }
  .appt__line--note { width: 62%; }
  .appt__days { display: flex; justify-content: space-between; margin: 16px 0 14px; }
  .appt__day { display: flex; align-items: center; gap: 4px; color: #888; font-size: 10px; }
  .appt__box { width: 20px; height: 16px; border: 1px solid #555; }
</style>
</head>
<body>

  <!-- Back: chiropractic text -->
  <section class="card card--info">
    <div class="wordmark"><span class="wordmark__main">BRIGHT PATH</span><span class="wordmark__sub">WELLNESS CENTRE</span></div>
    <div class="info__copy">
      <p>There is more to chiropractic than the relief of headaches and back pain! Our primary focus is the integrity of your nerve system, which controls and regulates every cell and tissue of your body. The moving bones of the spinal column can impair this vital communication link between your brain and body. We help improve the function and structure of your spine, reducing nerve system compromise. The result?</p>
      <p class="info__result">Even non-spinal related health problems can show improvement</p>
    </div>
    <div class="info__benefits">
      <span>Without drugs</span><span class="sep">|</span><span>Without surgery</span><span class="sep">|</span><span>Regardless of age</span><span class="sep">|</span><span>for over a century</span><span class="sep">|</span><span>Naturally</span>
    </div>
  </section>

  <!-- Front -->
  <section class="card card--front-1">
    <div class="wordmark"><span class="wordmark__main">BRIGHT PATH</span><span class="wordmark__sub">WELLNESS CENTRE</span></div>
    <div class="practitioner">
      <div class="practitioner__name">DR. MARTEN QUOVEL B.SC., D.C.</div>
      <div class="practitioner__title">CHIROPRACTOR</div>
    </div>
    <div class="front__rule"></div>
    <ul class="contacts">
      <li><svg viewBox="0 0 10 10"><path d="M2 0.5 L3.6 2.6 L2.8 3.6 Q4 6 6.4 7.2 L7.4 6.4 L9.5 8 L8.4 9.5 Q3 9 0.5 1.6Z"/></svg>416-872-0196 (PATH)</li>
      <li><svg viewBox="0 0 10 10"><circle cx="5" cy="5" r="4.5"/><path d="M0.5 5H9.5M5 0.5V9.5" stroke="#2c2c2c" stroke-width=".8"/></svg>www.brightpathwellnesscentre.example</li>
      <li><svg viewBox="0 0 10 10"><path d="M0.5 2H9.5V8H0.5Z"/><path d="M0.5 2L5 5.5L9.5 2" stroke="#2c2c2c" stroke-width=".8" fill="none"/></svg>brightpathchiro@mailbox.example</li>
    </ul>
    <address class="address">218 Farrow Gate<br>Larkmoor WC.<br>K2J 6P4</address>
  </section>

  <!-- Back: appointment card -->
  <section class="card card--appt">
    <svg class="appt__waves" viewBox="0 0 480 274" preserveAspectRatio="none" aria-hidden="true">
      <path d="M0 118 Q200 110 480 40 L480 274 L0 274Z" fill="var(--green)"/>
      <path d="M0 128 Q200 120 480 50 L480 274 L0 274Z" fill="var(--paper)"/>
      <path d="M300 274 Q400 230 480 205 L480 274Z" fill="#2c2c2c"/>
      <path d="M312 274 Q410 238 480 218 L480 274Z" fill="var(--green)"/>
    </svg>
    <div class="wordmark"><span class="wordmark__main">BRIGHT PATH</span><span class="wordmark__sub">WELLNESS CENTRE</span></div>
    <div class="appt__form">
      <div class="appt__line"><span>Name :</span><span class="fill"></span></div>
      <div class="appt__days">
        <div class="appt__day"><span class="appt__box"></span>M</div>
        <div class="appt__day"><span class="appt__box"></span>Tu</div>
        <div class="appt__day"><span class="appt__box"></span>W</div>
        <div class="appt__day"><span class="appt__box"></span>Th</div>
        <div class="appt__day"><span class="appt__box"></span>F</div>
        <div class="appt__day"><span class="appt__box"></span>Sat</div>
      </div>
      <div class="appt__line appt__line--note"><span>Note :</span><span class="fill"></span></div>
    </div>
  </section>

  <!-- Front (repeat) -->
  <section class="card card--front-2">
    <div class="wordmark"><span class="wordmark__main">BRIGHT PATH</span><span class="wordmark__sub">WELLNESS CENTRE</span></div>
    <div class="practitioner">
      <div class="practitioner__name">DR. MARTEN QUOVEL B.SC., D.C.</div>
      <div class="practitioner__title">CHIROPRACTOR</div>
    </div>
    <div class="front__rule"></div>
    <ul class="contacts">
      <li><svg viewBox="0 0 10 10"><path d="M2 0.5 L3.6 2.6 L2.8 3.6 Q4 6 6.4 7.2 L7.4 6.4 L9.5 8 L8.4 9.5 Q3 9 0.5 1.6Z"/></svg>416-872-0196 (PATH)</li>
      <li><svg viewBox="0 0 10 10"><circle cx="5" cy="5" r="4.5"/><path d="M0.5 5H9.5M5 0.5V9.5" stroke="#2c2c2c" stroke-width=".8"/></svg>www.brightpathwellnesscentre.example</li>
      <li><svg viewBox="0 0 10 10"><path d="M0.5 2H9.5V8H0.5Z"/><path d="M0.5 2L5 5.5L9.5 2" stroke="#2c2c2c" stroke-width=".8" fill="none"/></svg>brightpathchiro@mailbox.example</li>
    </ul>
    <address class="address">218 Farrow Gate<br>Larkmoor WC.<br>K2J 6P4</address>
  </section>

</body>
</html>
```